Neues Erscheinungsbild für Veranstaltungsreihe gesucht
Auch über das Projekt hinaus ist Matthias schon längere Zeit für uns tätig. Vielen Dank! :-)
Zielgruppe
Wir sind ein kleines Unternehmen, das Events in verschiedenen Städten Deutschlands plant und durchführt. Spezialisiert sind wir auf die Event-Reihe 'Wolkenreigen', bei denen drei Pyrotechniker gegeneinander antreten und in einem Wettstreit um das beste musiksynchrone Feuerwerk um den Sieg kämpfen. Bevor diese den Himmel erleuchten, rundet ein Rahmenprogramm bestehend aus Live-Bands, Feuerspucker-Shows, Kinder-Animation und einem großen kulinarischen Angebot den Abend ab.
Besuchen Sie die Website oder die Facebook-Seite (https://www.plaudernetz-beispiel.de/pages/Wolkenreigen/482715593027461), um sich ein Bild von der Veranstaltung zu machen.
Aufgabenstellung
Für die oben angesprochene Veranstaltungsreihe mit dem Namen 'Wolkenreigen' benötigen wir ein neues Plakatdesign.
Die Plakate soll auffallen, gut lesbar sein und ins Auge springen, aber dennoch nicht billig aussehen. Beim Betrachten soll direkt klar werden, dass es um Feuerwerk geht.
Auch bei längerer Sonneneinstrahlung auf die Plakate und dem damit einhergehenden Ausbleichen soll der Kontrast der Schrift noch groß sein.
Dieses Projekt ist ein Versuch, nach dessen Ablauf es nicht bei dem Gestalten des Plakates bleibt.
Wenn uns ein Design gefällt, benötigen wir darüber hinaus an andere Formate (A2, 18/1 Plakatwand, 3x2m Plakatwand) angepasste Plakate, ggfs. davon abgeleitete Flyer A6, von den Plakatwänden abgeleitete Banner 4x1m sowie von den Plakaten abgeleitetes Profilfoto und ein Timeline-Foto für Facebook.
Desweiteren benötigen wir eine neue Homepage mit CMS (WordPress, Joomla, Typo3, etc.), sodass Infos, Bilder, Videos und auch neue Veranstaltungen im nächsten Jahr selbst eingepflegt werden können.
Diese Folgeaufträge würden wir dann direkt vergeben.

```html
<!DOCTYPE html>
<html lang="de">
<head>
<meta charset="utf-8">
<title>Wolkenreigen – Plakat</title>
<link rel="stylesheet" href="https://fonts.googleapis.com/css2?family=Archivo+Black&family=Didact+Gothic&family=PT+Sans:wght@400;700&display=swap">
<style>
  :root {
    --night: #0b0706;
    --gold-top: #ffe23a;
    --gold-bottom: #f28a0c;
    --band-orange: #f7a21c;
    --band-rim: #e8650f;
    --ink: #1a1208;
    --white: #ffffff;
    --brand-orange: #ef7d1a;
  }
  * { margin: 0; padding: 0; box-sizing: border-box; }
  html, body { width: 848px; height: 1200px; overflow: hidden; background: var(--white); }
  .poster { position: relative; width: 848px; height: 1200px; overflow: hidden; background: var(--night); }

  .fireworks-photo {
    position: absolute; inset: 0 0 120px 0;
    background:
      radial-gradient(circle at 12% 16%, rgba(120,80,230,.85) 0, rgba(80,50,180,.4) 14%, transparent 26%),
      radial-gradient(circle at 42% 10%, rgba(240,200,140,.7) 0, rgba(200,140,70,.35) 16%, transparent 28%),
      radial-gradient(circle at 82% 14%, rgba(240,90,40,.75) 0, rgba(200,60,20,.35) 15%, transparent 28%),
      radial-gradient(circle at 50% 30%, rgba(230,130,50,.6) 0, transparent 30%),
      radial-gradient(circle at 20% 58%, rgba(220,120,50,.55) 0, transparent 24%),
      radial-gradient(circle at 80% 55%, rgba(210,190,110,.45) 0, transparent 24%),
      radial-gradient(circle at 75% 78%, rgba(90,200,110,.55) 0, transparent 18%),
      radial-gradient(circle at 93% 80%, rgba(230,60,60,.5) 0, transparent 14%),
      radial-gradient(circle at 22% 82%, rgba(230,140,60,.45) 0, transparent 20%),
      var(--night);
  }

  .headline { position: absolute; left: 0; right: 0; text-align: center; }
  .title {
    top: 290px;
    font-family: "Archivo Black", sans-serif;
    font-size: 100px; line-height: 1; letter-spacing: -1px;
    background: linear-gradient(180deg, var(--gold-top) 20%, var(--gold-bottom) 90%);
    -webkit-background-clip: text; background-clip: text; color: transparent;
    -webkit-text-stroke: 2px #2a1500;
    filter: drop-shadow(4px 5px 0 #000) drop-shadow(0 0 6px rgba(0,0,0,.7));
  }
  .subtitle {
    top: 397px; left: 40px;
    font-family: "Didact Gothic", sans-serif; font-weight: 400;
    font-size: 29px; color: var(--white);
    -webkit-text-stroke: .6px var(--white);
    text-shadow: 2px 2px 0 #000, -1px -1px 0 #000, 1px -1px 0 #000, -1px 1px 0 #000;
  }

  .venue {
    position: absolute; left: 52px; top: 470px;
    font-family: "Archivo Black", sans-serif;
    font-size: 54px; line-height: 62px; color: var(--white);
    text-shadow: 3px 3px 0 #000, -2px -2px 0 #000, 2px -2px 0 #000, -2px 2px 0 #000, 4px 5px 4px rgba(0,0,0,.8);
  }
  .venue span { display: block; }
  .venue .city { margin-left: -12px; }

  .date {
    position: absolute; left: 384px; top: 448px;
    font-family: "Archivo Black", sans-serif;
    font-size: 66px; line-height: 1; color: var(--white); letter-spacing: 1px;
    text-shadow: 3px 3px 0 #000, -2px -2px 0 #000, 2px -2px 0 #000, -2px 2px 0 #000, 4px 5px 4px rgba(0,0,0,.8);
  }
  .schedule {
    position: absolute; left: 402px; top: 518px;
    font-family: "PT Sans", sans-serif; font-weight: 700;
    font-size: 15.5px; line-height: 24px; color: var(--white);
    text-shadow: 1px 1px 0 #000, -1px -1px 0 #000, 1px -1px 0 #000, -1px 1px 0 #000;
  }

  .info-band { position: absolute; left: 0; top: 845px; width: 848px; height: 240px; }
  .info-band svg { position: absolute; inset: 0; }
  .info-text {
    position: absolute; left: 0; right: 0; top: 70px; text-align: center;
    font-family: "PT Sans", sans-serif; color: var(--ink);
  }
  .info-lead { font-weight: 700; font-size: 16.5px; }
  .info-links { font-weight: 700; font-size: 23px; margin-top: 10px; }
  .info-rule { width: 336px; height: 2px; background: var(--ink); margin: 9px auto 8px; }
  .prices { font-weight: 700; font-size: 13.5px; line-height: 17px; padding: 0 40px; }

  .sales-footer { position: absolute; left: 0; top: 1085px; width: 848px; height: 115px; background: var(--white); }
  .ticket-brand {
    position: absolute; left: 66px; top: 30px;
    display: flex; align-items: center; gap: 8px;
    font-family: "PT Sans", sans-serif; font-weight: 400;
    font-size: 30px; color: var(--brand-orange);
  }
  .ticket-brand .mark { width: 12px; height: 12px; border-radius: 50%; background: var(--brand-orange); }
  .sales-points {
    position: absolute; left: 264px; top: 30px;
    font-family: "PT Sans", sans-serif; font-weight: 700;
    font-size: 13.5px; line-height: 19.5px; color: var(--ink);
  }
</style>
</head>
<body>
<main class="poster">
  <div class="fireworks-photo" role="img" aria-label="Nachthimmel voller bunter Feuerwerksfontänen in Violett, Gold, Orange, Rot und Grün"></div>

  <h1 class="headline title">Wolkenreigen</h1>
  <p class="headline subtitle">Der große Wettstreit der Pyrotechniker</p>

  <p class="venue"><span>Schloss</span><span>Erlenhain</span><span class="city">Talbrück</span></p>
  <p class="date">12.03.2014</p>
  <p class="schedule">Einlass am 17.00 UHR<br>Beginn des Rahmenprogrammes am 18:00 Uhr</p>

  <section class="info-band">
    <svg width="848" height="240" viewBox="0 0 848 240" aria-hidden="true">
      <path d="M0 55 Q424 -40 848 55 L848 240 L0 240 Z" fill="var(--band-rim)"/>
      <path d="M0 68 Q424 -22 848 68 L848 240 L0 240 Z" fill="var(--band-orange)"/>
      <rect x="0" y="226" width="848" height="14" fill="var(--band-rim)"/>
    </svg>
    <div class="info-text">
      <p class="info-lead">Mehr Infor unter:</p>
      <p class="info-links">plaudernetz-beispiel.de/Wolkenreigen // www.wolkenreigen-wettbewerb.de</p>
      <div class="info-rule"></div>
      <p class="prices">Eintritspreise im Vorverkauf:<br>Jugendliche (von 12 bis 18 Jahren): 6,50€ // Erwachsene (ab 18 Jahren) 9,50€ zzgl. Vorverkaufge-<br>bühren. Kinder unter 12 Jahren haben im Stehplatzbereich freien Eintritt.</p>
    </div>
  </section>

  <footer class="sales-footer">
    <div class="ticket-brand"><span class="mark"></span>Kartenwerk</div>
    <p class="sales-points">WK-Stellen: Talbrücker Kartenhaus, Karten-Schnell,<br>LM-Laden Schloss Erlenhain, Evenora u.a. Ticket-Hotline: 01805 - 4400210<br>(0,14 €/ Minute, Mobil-Tel. ax. 0,24€/Minuten)</p>
  </footer>
</main>
</body>
</html>
```